I need a business card representing my company, VELDAR, it's an artist management and design company. Complete name is "VELDAR Artist Mgmt. + Design Co." I need it to be world class and very appealing, sophisticated and artistically unique.
Updates

Posted an updated Brief please see. I need a business card representing my company, VELDAR, it's an artist management and design company. Complete name is "VELDAR Artist Mgmt. + Design Co." I need it to be world class and very appealing, sophisticated and artistically unique.

Designs look the same

Designs look the same

Target Market(s)

Advertisers, Entertainment Companies, Commercial companies

Industry/Entity Type

Advertising

Contact Information for Business Card

I need a business card representing my company, VELDAR, it's an artist management and design company. Complete name is "VELDAR Artist Mgmt. + Design Co." I need it to be world class and very appealing, sophisticated and artistically unique. One side can be VELDAR Artist Mgmt. + Design Co. and the other my name, Theodore Quillan, my contact telephone: 415.638.2097, email veldarartist@mailnest.example, my address: 2416 Harrowgate Ave. #317 Miami, FL 33152

Font styles to use
Other font styles liked:
• Calibri

Colors
ffffff
0455a3
f37122

Requirements
Must have
• "VELDAR" stand out bigger than the rest of the text.
Nice to have
• Name "VELDAR" can be centered on one side or in the corner or along side edges, just need something cool and different.
Should not have
• I am open just try to keep it clean looking

```html
<!DOCTYPE html>
<html lang="en">
<head>
<meta charset="utf-8">
<title>VELDAR Business Card – Print Layout</title>
<link href="https://fonts.googleapis.com/css2?family=Oswald:wght@300;600&family=Barlow:wght@400&display=swap" rel="stylesheet">
<style>
  :root {
    --paper: #ffffff;
    --card-dark: #141414;
    --card-mid: #2a2a2a;
    --ink-light: #ffffff;
    --crop: #444444;
  }
  html, body {
    margin: 0;
    padding: 0;
    width: 1200px;
    height: 1200px;
    overflow: hidden;
    background: var(--paper);
  }
  .sheet {
    position: relative;
    width: 1200px;
    height: 1200px;
    background: var(--paper);
  }
  .crop-marks {
    position: absolute;
    inset: 0;
  }
  .card {
    position: absolute;
    top: 230px;
    width: 386px;
    height: 675px;
    overflow: hidden;
    background: radial-gradient(ellipse at 50% 45%, var(--card-mid) 0%, var(--card-dark) 75%);
    color: var(--ink-light);
  }
  .card--front { left: 144px; }
  .card--back  { left: 670px; }
  .card__texture {
    position: absolute;
    inset: 0;
  }
  .brand-name {
    position: absolute;
    left: 30px;
    top: 70px;
    margin: 0;
    font-family: "Oswald", sans-serif;
    font-weight: 600;
    font-size: 58px;
    line-height: 1;
    letter-spacing: 1px;
  }
  .brand-tagline {
    position: absolute;
    left: 30px;
    top: 130px;
    margin: 0;
    font-family: "Oswald", sans-serif;
    font-weight: 300;
    font-size: 29px;
    line-height: 1;
  }
  .person-name {
    position: absolute;
    margin: 0;
    font-family: "Oswald", sans-serif;
    font-weight: 600;
    font-size: 39px;
    line-height: 1;
    white-space: nowrap;
  }
  .card--front .person-name { left: 29px; top: 579px; }
  .card--back  .person-name { right: 32px; top: 67px; }
  .contact-list {
    position: absolute;
    right: 86px;
    top: 503px;
    margin: 0;
    padding: 0;
    list-style: none;
    font-family: "Barlow", sans-serif;
    font-size: 16px;
    line-height: 20px;
    text-align: right;
  }
  .contact-list li { margin-bottom: 12px; }
  .contact-list li.contact--phone { margin-bottom: 14px; }
  .contact-rule {
    position: absolute;
    left: 319px;
    top: 508px;
    width: 2px;
    height: 112px;
    background: var(--ink-light);
  }
  .contact-icons {
    position: absolute;
    left: 330px;
    top: 510px;
  }
</style>
</head>
<body>
<div class="sheet">
  <svg class="crop-marks" width="1200" height="1200" viewBox="0 0 1200 1200" aria-hidden="true">
    <g stroke="var(--crop)" stroke-width="1">
      <line x1="144.5" y1="86" x2="144.5" y2="182"/>
      <line x1="529.5" y1="86" x2="529.5" y2="182"/>
      <line x1="670.5" y1="86" x2="670.5" y2="182"/>
      <line x1="1055.5" y1="86" x2="1055.5" y2="182"/>
      <line x1="144.5" y1="954" x2="144.5" y2="1050"/>
      <line x1="529.5" y1="954" x2="529.5" y2="1050"/>
      <line x1="670.5" y1="954" x2="670.5" y2="1050"/>
      <line x1="1055.5" y1="954" x2="1055.5" y2="1050"/>
      <line x1="0" y1="230.5" x2="96" y2="230.5"/>
      <line x1="1104" y1="230.5" x2="1200" y2="230.5"/>
      <line x1="0" y1="904.5" x2="96" y2="904.5"/>
      <line x1="1104" y1="904.5" x2="1200" y2="904.5"/>
      <line x1="578" y1="230.5" x2="622" y2="230.5"/>
      <line x1="578" y1="904.5" x2="622" y2="904.5"/>
    </g>
  </svg>

  <section class="card card--front">
    <div class="card__texture" role="img" aria-label="Dark woven basket-weave texture background"></div>
    <h1 class="brand-name">VELDAR</h1>
    <p class="brand-tagline">Artist Mgmt. + Design Co.</p>
    <p class="person-name">Theodore Quillan</p>
  </section>

  <section class="card card--back">
    <div class="card__texture" role="img" aria-label="Dark woven basket-weave texture background"></div>
    <p class="person-name">Theodore Quillan</p>
    <ul class="contact-list">
      <li class="contact--phone">415 638 2097</li>
      <li class="contact--address">2416 Harrowgate Ave.<br>#317 Miami, FL 33152</li>
      <li class="contact--email">veldarartist@mailnest.example</li>
    </ul>
    <div class="contact-rule"></div>
    <svg class="contact-icons" width="20" height="110" viewBox="0 0 20 110" aria-hidden="true">
      <g fill="#ffffff">
        <circle cx="10" cy="11" r="8"/>
        <circle cx="10" cy="56" r="8"/>
        <circle cx="10" cy="98" r="8"/>
      </g>
      <g fill="none" stroke="#1a1a1a" stroke-width="1.4" stroke-linejoin="round">
        <rect x="7.5" y="6.5" width="5" height="9" rx="1"/>
        <path d="M6 57 L10 53 L14 57 M7 56.5 V60 H13 V56.5"/>
        <circle cx="10" cy="98" r="4"/>
        <path d="M6 98 H14 M10 94 C8 96 8 100 10 102 C12 100 12 96 10 94"/>
      </g>
    </svg>
  </section>
</div>
</body>
</html>
```